Craft oriented film company needs a Business Card design

Hi all,
We're a 2-man band film company in New Zealand called Brindle Pictures. We're good honest blokes, who are very passionate about the craft of film making. I've attached our current logo which has a bit of a crafty/artisan feel that we like. Feel free to use it - or throw the baby out with the bathwater and start again..... you never know, you might inspire a complete brand re-work.

In any case, the vibe we want to give out is that we are solid, dependable and no bullshit - but without compromising creative excellence and being in the now. We like the 'Brooklyn' artisan style of work.

Preferably single sided.

We need the standard stuff:
Name, job title, cellphone, email address and physical address (this can be smaller if you like - street, suburb, city & zip, country [if you want])

Check out our website to learn more about us: brindlepictures.example

Target Market(s)

Brand marketers and advertising agency creatives looking for video production.

Requirements
Should not have
• Nothing flashy or too 'futuristic', we want it to feel grounded and real. A limited colour palette is preferred.
We don't want any film reels or cameras or anything obvious like that.

```html
<!DOCTYPE html>
<html lang="en">
<head>
<meta charset="utf-8">
<title>Brindle Pictures – Business Card</title>
<link href="https://fonts.googleapis.com/css2?family=Rokkitt:wght@700&family=Ubuntu+Condensed&family=Yellowtail&display=swap" rel="stylesheet">
<style>
  :root {
    --backdrop: #dde2e6;
    --card: #f4f3ef;
    --ink: #2a2623;
    --ink-soft: #3a3531;
    --accent: #8c1f1f;
    --pattern-tone: #d9d7d2;
  }
  * { box-sizing: border-box; margin: 0; padding: 0; }
  html, body { width: 1200px; height: 1000px; overflow: hidden; }
  body {
    background: var(--backdrop);
    position: relative;
    font-family: "Ubuntu Condensed", "Arial Narrow", sans-serif;
    color: var(--ink);
  }
  .card {
    position: absolute;
    left: 360px; top: 140px;
    width: 480px; height: 720px;
    background: var(--card);
    box-shadow: 0 2px 6px rgba(0,0,0,0.12);
  }
  .brand-band {
    position: absolute;
    left: 24px; top: 14px;
    width: 432px; height: 356px;
    background: linear-gradient(135deg, var(--pattern-tone), #e6e4df 50%, var(--pattern-tone));
  }
  .brand {
    position: absolute;
    left: 24px; top: 14px;
    width: 432px; height: 356px;
    display: flex; align-items: center; justify-content: center; gap: 12px;
  }
  .brand-dot {
    flex: 0 0 18px;
    width: 18px; height: 18px; border-radius: 50%;
    background: var(--ink);
  }
  .brand-name {
    font-family: "Rokkitt", Georgia, serif;
    font-weight: 700;
    font-size: 34px;
    letter-spacing: 0.02em;
    white-space: nowrap;
    color: var(--ink);
    text-transform: uppercase;
  }
  .person {
    position: absolute;
    left: 0; top: 382px; width: 480px; height: 70px;
    text-align: center;
  }
  .person-name {
    font-family: "Rokkitt", Georgia, serif;
    font-weight: 700;
    font-size: 40px;
    letter-spacing: 0.2em;
    white-space: nowrap;
    color: var(--ink);
    line-height: 1;
  }
  .person-role {
    position: absolute;
    left: 236px; top: 34px;
    font-family: "Yellowtail", cursive;
    font-size: 20px;
    line-height: 1;
    color: var(--accent);
  }
  .rule {
    position: absolute;
    left: 40px; width: 400px;
    border-top: 3px dotted var(--ink-soft);
  }
  .rule-1 { top: 473px; }
  .rule-2 { top: 556px; }
  .rule-3 { top: 637px; }
  .contact-row {
    position: absolute;
    left: 40px; top: 480px; width: 400px; height: 70px;
    display: flex; align-items: center;
    font-size: 16px;
    white-space: nowrap;
  }
  .contact-phone { flex: 0 0 150px; text-align: left; }
  .contact-phone .brace { color: var(--accent); }
  .contact-divider {
    flex: 0 0 0;
    height: 40px;
    border-left: 3px dotted var(--ink-soft);
  }
  .contact-email { flex: 1; text-align: right; padding-left: 16px; }
  .address {
    position: absolute;
    left: 0; top: 570px; width: 480px;
    text-align: center;
    font-size: 18px;
    font-style: normal;
    line-height: 29px;
  }
  .address .sep { color: var(--accent); font-size: 14px; }
  .website {
    position: absolute;
    left: 0; top: 658px; width: 480px;
    text-align: center;
    font-size: 18px;
  }
  .website .domain { color: var(--accent); }
</style>
</head>
<body>
  <main class="card">
    <div class="brand-band" role="img" aria-label="Fine diagonal line pattern behind the company badge"></div>
    <div class="brand">
      <span class="brand-dot"></span>
      <span class="brand-name">Brindle Pictures</span>
    </div>

    <section class="person">
      <h1 class="person-name">TOMAS REID</h1>
      <span class="person-role">director</span>
    </section>

    <div class="rule rule-1"></div>
    <div class="contact-row">
      <span class="contact-phone"><span class="brace">{</span>+64.21.55.0199<span class="brace">}</span></span>
      <span class="contact-divider"></span>
      <span class="contact-email">tomas@brindlepictures.example</span>
    </div>
    <div class="rule rule-2"></div>

    <address class="address">
      18 Kereru Lane <span class="sep">›</span> Harbour View<br>
      Auckland <span class="sep">›</span> New Zealand 1024
    </address>
    <div class="rule rule-3"></div>

    <p class="website">http://<span class="domain">www.brindlepictures.example</span></p>
  </main>
</body>
</html>
```